Banner Ad Design Project: rovalenmotors.com

Google all ad dimensions banner pack for http://www.rovalenmotors.com.

Ad dimensions Max. file sizes (KB) Ad types
468 × 60 50 Banner
728 × 90 50 Leaderboard
250 × 250 50 Square
200 × 200 50 Small square
336 × 280 50 Large rectangle
300 × 250 50 Inline rectangle
120 × 600 50 Skyscraper
160 × 600 50 Wide skyscraper
300 × 600 200 Half-page ad
970 × 90 200 Large leaderboard
240 × 400 50 Vertical rectangle
980 × 120 200 Panorama
930 × 180 200 Top banner
250 × 360 50 Triple widescreen
580 × 400 200 Netboard

*Please visit the website and come up with unique ideas.

Target Market(s)

Consumers looking to transport a car, motor vehicle, motorcycle or anything that has wheels and a motor in the united states long distance.

Industry/Entity Type

Google

Requirements
Must have
• a call to action for example (RANDOM ONE):
-
TALK TO A REAL CAR SHIPPING PRO NOW: 1-888-514-2763
HAVE CAR TRANSPORT QUESTIONS? CALL NOW: 1-888-514-2763
CALL NOW & TALK TO A REAL AUTO SHIPPING EXPERT: 1-888-514-2763
Call Now Free Quote:1-888-514-2763

Nice to have
• Best Value For Dollar Auto Transport
Bonded, Insured & Licensed
Price Match Guarantee: will match any price by a 4 or 5 star rated Company.
Best of all, you pay nothing until your car is picked up!
Nationwide Door-To-Door Vehicle Shipping
Should not have
• Logo integrated in to the design.
bold call to action; ex; call now free quote:
Heading style phone number, 888-514-2763, stands out and screams call now.
example:
CALL ROVALEN TODAY TO TRANSPORT YOUR VEHICLE
1-888-514-2763

```html
<!DOCTYPE html>
<html lang="en">
<head>
<meta charset="utf-8">
<title>Rovalen Motors – Netboard Banner</title>
<link rel="stylesheet" href="https://fonts.googleapis.com/css2?family=Montserrat:wght@600;700;800&display=swap">
<style>
  :root {
    --ink: #2b2b2d;
    --red: #e0202a;
    --slate: #58585a;
    --paper-top: #ffffff;
    --paper-bottom: #e4e4e6;
    --white: #ffffff;
    --bullet: #4a4a4c;
  }
  html, body {
    margin: 0;
    padding: 0;
    width: 1200px;
    height: 797px;
    overflow: hidden;
  }
  .banner {
    position: relative;
    width: 1200px;
    height: 797px;
    overflow: hidden;
    background: linear-gradient(180deg, var(--paper-top) 0%, #f1f1f2 45%, var(--paper-bottom) 100%);
    font-family: "Montserrat", Arial, sans-serif;
    color: var(--ink);
  }
  .headline {
    position: absolute;
    left: 0;
    right: 0;
    top: 46px;
    margin: 0;
    text-align: center;
    font-weight: 700;
    text-transform: uppercase;
    line-height: 1;
  }
  .headline .lead {
    display: block;
    font-size: 78px;
    letter-spacing: 0.5px;
    color: var(--ink);
  }
  .headline .accent-line {
    display: block;
    margin-top: 22px;
    font-size: 94px;
    color: var(--red);
  }
  .headline .accent-line .article {
    color: var(--ink);
    font-size: 80px;
  }
  .headline .accent-line + .accent-line {
    margin-top: 12px;
  }
  .phone-row {
    position: absolute;
    left: 0;
    right: 0;
    top: 338px;
    height: 90px;
  }
  .phone-row .rule {
    position: absolute;
    top: 36px;
    width: 200px;
    height: 14px;
  }
  .phone-row .rule-left { left: 64px; }
  .phone-row .rule-right { right: 66px; }
  .phone-number {
    position: absolute;
    left: 0;
    right: 0;
    top: 0;
    margin: 0;
    text-align: center;
    font-size: 80px;
    font-weight: 700;
    line-height: 90px;
    color: var(--ink);
    letter-spacing: 1px;
  }
  .brand {
    position: absolute;
    left: 18px;
    top: 540px;
    width: 480px;
    height: 200px;
  }
  .brand-art {
    position: absolute;
    left: 0;
    top: 30px;
    width: 220px;
    height: 150px;
    border-radius: 6px;
    background: linear-gradient(160deg, #d6d7da 0%, #b9bbc0 100%);
  }
  .brand-name {
    position: absolute;
    left: 232px;
    top: 116px;
    margin: 0;
    font-size: 44px;
    font-weight: 700;
    color: var(--ink);
    letter-spacing: 1px;
  }
  .benefits {
    position: absolute;
    left: 556px;
    top: 505px;
    width: 620px;
    margin: 0;
    padding: 0;
    list-style: none;
    font-size: 27px;
    font-weight: 700;
    color: var(--ink);
    line-height: 50px;
  }
  .benefits li {
    position: relative;
    padding-left: 44px;
    margin-bottom: 8px;
  }
  .benefits li::before {
    content: "";
    position: absolute;
    left: 0;
    top: 15px;
    width: 20px;
    height: 20px;
    border-radius: 50%;
    background: var(--bullet);
  }
  .footer-band {
    position: absolute;
    left: 0;
    bottom: 0;
    width: 1200px;
    height: 60px;
  }
  .footer-band svg {
    position: absolute;
    inset: 0;
  }
  .website {
    position: absolute;
    left: 0;
    width: 1020px;
    top: 0;
    margin: 0;
    text-align: center;
    line-height: 60px;
    font-size: 40px;
    font-weight: 700;
    color: var(--white);
  }
</style>
</head>
<body>
  <main class="banner">
    <h1 class="headline">
      <span class="lead">Call Now &amp; Talk To</span>
      <span class="accent-line"><span class="article">A</span> Real Auto</span>
      <span class="accent-line">Shipping Expert</span>
    </h1>

    <div class="phone-row">
      <svg class="rule rule-left" viewBox="0 0 200 14" aria-hidden="true">
        <polygon points="0,7 24,0 200,0 200,14 24,14" fill="var(--red)"/>
      </svg>
      <p class="phone-number">1-888-514-2763</p>
      <svg class="rule rule-right" viewBox="0 0 200 14" aria-hidden="true">
        <polygon points="0,0 176,0 200,7 176,14 0,14" fill="var(--red)"/>
      </svg>
    </div>

    <div class="brand">
      <div class="brand-art" role="img" aria-label="Sketch of a car transport truck"></div>
      <p class="brand-name">ROVALEN</p>
    </div>

    <ul class="benefits">
      <li>Best Value For Dottar Auto Transport</li>
      <li>Bonded, Insured &amp; Licensed</li>
      <li>Nationalwide Door-To-Door Vehicle Shipping</li>
    </ul>

    <div class="footer-band">
      <svg viewBox="0 0 1200 60" width="1200" height="60" aria-hidden="true">
        <rect x="0" y="0" width="1200" height="60" fill="var(--slate)"/>
        <polygon points="0,0 1040,0 995,60 0,60" fill="var(--red)"/>
      </svg>
      <p class="website">www.rovalenmotors.com</p>
    </div>
  </main>
</body>
</html>
```